Australian Recruitment Agency Flyer

We are looking for a 1 page flyer to promote our recruitment company. We would like this to have a corporate look.

Attached is a word document with the content we would like included in the flyer.

I have also attached some of our clients logos to be included in the flyer

Target Market(s)

Professional organisations looking to hire new staff

Industry/Entity Type

It Company

Colors
85abd2
3176b5
31b7a3
d2a4cc
e667a6
b768aa
876aae
3276b5
f04a50

Requirements
Must have
• Must have the content that we have include on a word document in the design brief.

```html
<!DOCTYPE html>
<html lang="en">
<head>
<meta charset="utf-8">
<title>TalentBridge Recruitment Flyer</title>
<link href="https://fonts.googleapis.com/css2?family=Barlow+Condensed:wght@600;700&family=Montserrat:ital,wght@0,300;0,400;0,600;1,300&display=swap" rel="stylesheet">
<style>
  :root {
    --brand-blue: #3176b5;
    --deep-blue: #1f5a9e;
    --sky: #85abd2;
    --pale: #dbe8f5;
    --ink: #1d1f24;
    --muted: #4a5564;
    --accent-teal: #31b7a3;
    --white: #ffffff;
  }
  * { margin: 0; padding: 0; box-sizing: border-box; }
  html, body { width: 849px; height: 1200px; overflow: hidden; background: #e9ebee; }
  .flyer {
    position: relative; width: 849px; height: 1200px; overflow: hidden;
    background: var(--white);
    font-family: "Montserrat", sans-serif; color: var(--ink);
  }
  .header {
    position: absolute; top: 0; left: 0; width: 100%; height: 175px;
    display: flex; justify-content: center; align-items: center;
  }
  .brand { display: flex; align-items: center; gap: 14px; }
  .brand-square { width: 44px; height: 44px; background: var(--brand-blue); }
  .brand-text { display: flex; flex-direction: column; }
  .brand-name { font-size: 36px; font-weight: 600; color: var(--brand-blue); line-height: 1; }
  .brand-tag { font-size: 10px; color: var(--brand-blue); margin-top: 5px; letter-spacing: .3px; }

  .hero {
    position: absolute; top: 175px; left: 0; width: 100%; height: 455px;
  }
  .hero-photo {
    position: absolute; inset: 0;
    background: linear-gradient(90deg, #15181e 0%, #2a2f3a 30%, #3f5f86 48%, #2c68ad 62%, var(--deep-blue) 100%);
  }
  .hero-copy {
    position: absolute; right: 36px; top: 22px; text-align: right;
    font-family: "Barlow Condensed", sans-serif; font-weight: 700;
    color: var(--white); text-transform: uppercase; line-height: 1.12;
  }
  .hero-copy .line { display: block; font-size: 42px; }
  .hero-copy .line-big { font-size: 62px; line-height: 1; }
  .testimonial {
    position: absolute; right: 36px; top: 318px; width: 330px; text-align: right;
    color: #dfe9f6; font-size: 12px; line-height: 1.35;
  }
  .testimonial q { font-style: italic; font-weight: 300; quotes: "\201C" "\201D"; }
  .testimonial .author { display: block; margin-top: 8px; font-weight: 600; font-size: 11px; }
  .testimonial .role { display: block; font-size: 10px; font-weight: 300; }

  .services {
    position: absolute; top: 630px; left: 0; width: 100%; height: 370px;
    background: linear-gradient(180deg, #8fb4dc 0%, #c2d7ee 35%, var(--pale) 70%, #f6f9fc 100%);
    text-align: center;
  }
  .badge {
    position: absolute; left: 50%; transform: translateX(-50%);
    width: 206px; height: 40px; background: var(--brand-blue);
    clip-path: polygon(8% 0, 100% 0, 92% 100%, 0 100%);
    color: var(--white); font-family: "Barlow Condensed", sans-serif; font-weight: 700;
    font-size: 22px; line-height: 40px; text-transform: uppercase;
  }
  .badge-what { top: 42px; }
  .badge-industries { top: 228px; width: 260px; }
  .services p {
    position: absolute; left: 0; width: 100%;
    font-size: 14px; font-weight: 300; color: var(--muted); line-height: 1.55;
  }
  .about { top: 105px; }
  .industries { top: 290px; }

  .clients-heading, .closing {
    position: absolute; left: 0; width: 100%; text-align: center;
    font-family: "Barlow Condensed", sans-serif; font-weight: 700; text-transform: uppercase;
    color: var(--ink);
  }
  .clients-heading { top: 1008px; font-size: 22px; }
  .client-list {
    position: absolute; top: 1078px; left: 50px; right: 50px;
    display: flex; justify-content: space-between; align-items: center;
    list-style: none;
  }
  .client-list li { font-size: 13px; font-weight: 600; color: var(--muted); }
  .closing { top: 1140px; font-size: 21px; }
</style>
</head>
<body>
<main class="flyer">
  <header class="header">
    <div class="brand">
      <span class="brand-square"></span>
      <div class="brand-text">
        <span class="brand-name">TalentBridge</span>
        <span class="brand-tag">Human Resources &amp; Recruitment</span>
      </div>
    </div>
  </header>

  <section class="hero">
    <div class="hero-photo" role="img" aria-label="Businessman in a dark suit reaching out for a handshake against a blue backdrop"></div>
    <h1 class="hero-copy">
      <span class="line">We have over</span>
      <span class="line line-big">20 years</span>
      <span class="line">of experience</span>
      <span class="line">helping companies</span>
      <span class="line">hire amazing talent</span>
    </h1>
    <blockquote class="testimonial">
      <q>TalentBridge really delivered on their promise and far exceeded our expectations. Their fixed fee model saved us thousands</q>
      <span class="author">Mark Dalton</span>
      <span class="role">General Manager</span>
      <span class="role">Kestrel Financial Services</span>
    </blockquote>
  </section>

  <section class="services">
    <h2 class="badge badge-what">What we do</h2>
    <p class="about">We aren't a recruitment agency, we are an extension of your team.<br>We become your very own HR &amp; Recruitment department to be called<br>upon as and when needed.</p>
    <h2 class="badge badge-industries">Industries we serve</h2>
    <p class="industries">Mining and Oil &amp; Gas &nbsp;|&nbsp; Accounting &amp; Finance &nbsp;|&nbsp; Sales &amp; Marketing<br>IT &amp; Communications &nbsp;|&nbsp; Government &amp; Not for Profit</p>
  </section>

  <h2 class="clients-heading">Start a conversation today and see why these companies</h2>
  <ul class="client-list">
    <li>Swiftfleet</li>
    <li>Keystone</li>
    <li>Basalt Minerals</li>
    <li>Southbank</li>
    <li>Larkspur</li>
    <li>Orvale</li>
    <li>Trellis</li>
  </ul>
  <p class="closing">Turn to us time and time again</p>
</main>
</body>
</html>
```